Business Card for premium dental clinic

We are a premium dental clinic based in Brasov, Romania with more than 15 year on the market, providing quality dental treatment made by a team of more specialized dentists, working with modern equipment as a solution to beautiful and healthy teeth.

Our current logo for the clinic use 2 square with colors black and gold - dr Corbescu - studio, using family fonts Bodoni, Myriad Pro and Segoe Print.
Depending on the printing we used some gold CMYK background or gold foil picture background or a gold gradient.
We want a business card:
- eye catching business card
- distinguished business card
- premium design
- to keep the color scheme of black and gold
- to attract the customers to spent time reading the information
- modern concept

```html
<!DOCTYPE html>
<html lang="en">
<head>
<meta charset="utf-8">
<title>dr Corbescu studio – business card</title>
<link href="https://fonts.googleapis.com/css2?family=Source+Sans+3:wght@400&family=Mulish:wght@400;500&display=swap" rel="stylesheet">
<style>
  :root {
    --page: #f4f4f4;
    --card-black: #000000;
    --gold: #b8923f;
    --gold-light: #d9b45a;
    --white: #ffffff;
    --divider: #8a8a8a;
    --photo-dark: #2a1a22;
    --photo-mid: #9b7a55;
    --photo-light: #b98a4c;
  }
  * { margin: 0; padding: 0; box-sizing: border-box; }
  html, body { width: 1200px; height: 1200px; overflow: hidden; background: var(--page); }
  .canvas { position: relative; width: 1200px; height: 1200px; }

  .card {
    position: absolute;
    left: 222px;
    width: 756px;
    height: 432px;
    border-radius: 22px;
    overflow: hidden;
  }
  .card--front { top: 124px; }
  .card--back { top: 644px; background: var(--card-black); }

  .front-photo {
    position: absolute; inset: 0;
    background:
      radial-gradient(ellipse 45% 40% at 48% 52%, #e9e4da 0%, rgba(233,228,218,0) 70%),
      linear-gradient(100deg, var(--photo-dark) 0%, #5a3f3a 30%, var(--photo-mid) 60%, var(--photo-light) 100%);
  }

  .brand-block {
    position: absolute;
    left: 491px; top: 288px;
    width: 222px; height: 109px;
    background: var(--card-black);
    border: 1px solid var(--white);
    display: flex; align-items: center; justify-content: center; gap: 10px;
  }
  .brand-block__square { width: 14px; height: 14px; background: var(--gold-light); }
  .brand-block__name {
    font-family: "Source Sans 3", sans-serif;
    font-weight: 400;
    font-size: 22px;
    color: var(--gold-light);
  }

  .identity {
    position: absolute;
    right: calc(756px - 274px);
    text-align: right;
    font-family: "Source Sans 3", sans-serif;
  }
  .identity__name {
    position: absolute; right: 0; top: 178px;
    white-space: nowrap;
    font-size: 38px; font-weight: 400; color: var(--white);
    letter-spacing: -0.5px;
  }
  .identity__role {
    position: absolute; right: 0; top: 232px;
    white-space: nowrap;
    font-family: "Mulish", sans-serif;
    font-size: 15.5px; color: var(--gold); letter-spacing: 1.3px;
  }

  .divider {
    position: absolute; left: 305px; top: 151px;
    width: 1px; height: 135px; background: var(--divider);
  }

  .contact-list { list-style: none; position: absolute; left: 336px; top: 156px; }
  .contact-list__item {
    display: flex; align-items: center; height: 33px;
    font-family: "Mulish", sans-serif; font-size: 15px; font-weight: 500;
    color: var(--gold); letter-spacing: 1.7px; white-space: nowrap;
  }
  .contact-list__icon { width: 16px; height: 16px; margin-right: 11px; fill: var(--white); flex: none; }
</style>
</head>
<body>
<main class="canvas">
  <section class="card card--front">
    <div class="front-photo" role="img" aria-label="Close-up photograph of lips with gold leaf holding a string of pearls"></div>
    <div class="brand-block">
      <span class="brand-block__square"></span>
      <span class="brand-block__name">dr Corbescu studio</span>
    </div>
  </section>

  <section class="card card--back">
    <div class="identity">
      <h1 class="identity__name">DR. CORBESCU</h1>
      <p class="identity__role">DENTAL SPECIALIST</p>
    </div>
    <div class="divider"></div>
    <ul class="contact-list">
      <li class="contact-list__item">
        <svg class="contact-list__icon" viewBox="0 0 16 16"><path d="M1 3h14v10H1z M2 4l6 5 6-5" fill="none" stroke="#fff" stroke-width="1.6"/></svg>
        studio@drcorbescu.ro
      </li>
      <li class="contact-list__item">
        <svg class="contact-list__icon" viewBox="0 0 16 16"><path d="M3.5 1.5l2.5 3-1.5 2c.9 2 2.6 3.6 4.6 4.6l2-1.5 3 2.5-1.4 2.2C6.8 14 1.9 9.2 1.3 3z"/></svg>
        +40 268 555 019
      </li>
      <li class="contact-list__item">
        <svg class="contact-list__icon" viewBox="0 0 16 16"><path d="M3 1l10 8-4.3.5 2.4 5-1.8.8-2.4-5L3 13z"/></svg>
        www.drcorbescu.ro
      </li>
      <li class="contact-list__item">
        <svg class="contact-list__icon" viewBox="0 0 16 16"><path d="M8 0.8a5.5 5.5 0 0 0-5.5 5.5C2.5 10.4 8 15.5 8 15.5s5.5-5.1 5.5-9.2A5.5 5.5 0 0 0 8 .8zm0 7.7a2.2 2.2 0 1 1 0-4.4 2.2 2.2 0 0 1 0 4.4z"/></svg>
        Strada Lungă 48, Brasov 500058
      </li>
    </ul>
  </section>
</main>
</body>
</html>
```